New Web Design for Texas Lawyer

We need to update the look of https://www.veltonbrisk.example/. Need to be same colors but new logo and style. Modern.
General Style and Professionalism
Maintain the general style that is liked.
Aim for a more formal and professional appearance.
Logo and Lawyer Information
Design a new logo.
Note that Lawyer Peter is no longer with the firm. The new lawyer should be prominently displayed on the right.
Homepage Features
Consider implementing a slider for video content.
Explore the idea of featuring 18 wheelers on the forefront of the homepage.
SEO Focus
Prioritize SEO efforts for Austin and the surrounding areas.
Design
Develop a new website design.
Ensure that testimonials are more prominently displayed on the homepage.
Core Values and Additional Content
Await core values information from Megan.
Add a TikTok link to the website.
Incorporate new photography to enhance the site's visual appeal.
Testimonials and Results
Create more compelling testimonials.
Highlight case results to make them more appealing.
Media Page
Improve the media page for a better user experience.
Firm Recognition
Emphasize the firm's status as an award-winning law firm.
Referral Program
Make the "referral program" more prominent.
Emphasize the message about passive income and always include the relevant rule.
Attorney Pages
Design a main page for the attorney.
Create subpages for other lawyers.
About the Law Firm
Design a comprehensive "About the Law Firm" page.
Our 5 core values:
Integrity (we live up to our word, we say what we mean and mean what we say; we’re honest)
Compassion (we put people FIRST; we listen because we care)
Trust (earned through respect and communication)
Advocacy (we are the voice of those who can’t speak on their own behalf; we do it through experience, competency and hard work)
Results (we aim to achieve the most it takes to make our clients whole)
Number of Pages Required
4 page
Look and feel
Each slider illustrates characteristics of the customer's brand and the style your logo design should communicate.

```html
<!DOCTYPE html>
<html lang="en">
<head>
<meta charset="utf-8">
<title>Velton Brisk Law, PLLC – Austin Accident Law Firm</title>
<link rel="stylesheet" href="https://fonts.googleapis.com/css2?family=Libre+Baskerville:wght@400;700&family=Open+Sans:wght@400;600;700&display=swap">
<style>
:root{
  --navy:#1d3b66;
  --navy-dark:#132a4c;
  --navy-deep:#0d1f3a;
  --red:#c9211e;
  --ink:#2d3440;
  --muted:#6b7280;
  --line:#d7dbe2;
  --paper:#ffffff;
  --mist:#f2f4f7;
  --serif:'Libre Baskerville',Georgia,serif;
  --sans:'Open Sans',Arial,sans-serif;
}
*{box-sizing:border-box;margin:0;padding:0}
html,body{width:1200px;height:4812px;overflow:hidden}
body{font-family:var(--sans);color:var(--ink);background:var(--paper);font-size:13px;line-height:1.6}
section,header,footer{position:relative;width:1200px;overflow:hidden}
.btn{display:inline-block;background:var(--red);color:#fff;font-family:var(--sans);font-weight:700;font-size:11px;letter-spacing:1px;text-transform:uppercase;padding:10px 22px;border-radius:2px;text-decoration:none}
.heading{font-family:var(--serif);color:var(--navy);text-transform:uppercase;text-align:center;font-weight:400;font-size:34px;letter-spacing:.5px}
.lead{width:660px;margin:0 auto;text-align:center;color:var(--muted);font-size:13.5px;line-height:1.75}

/* hero */
.hero{height:700px}
.hero-photo{position:absolute;inset:0;background:linear-gradient(180deg,#5d6f88 0%,#3f557a 45%,#24406b 100%)}
.hero-shade{position:absolute;inset:0;background:linear-gradient(180deg,rgba(19,42,76,.35),rgba(19,42,76,.75))}
.topbar{position:absolute;top:0;left:0;right:0;height:34px;background:rgba(255,255,255,.92);display:flex;align-items:center;justify-content:space-between;padding:0 150px}
.topbar .call{font-size:12px;color:var(--navy);font-weight:600}
.topbar .call b{color:var(--red);margin-left:8px}
.lang{display:flex;gap:14px;font-size:11px;color:var(--navy);font-weight:600}
.lang span::before{content:"";display:inline-block;width:14px;height:9px;background:var(--navy);margin-right:5px;vertical-align:-1px}
.lang span:last-child::before{background:var(--red)}
.nav{position:absolute;top:62px;left:145px;right:145px;height:36px;background:rgba(19,42,76,.85);display:flex;align-items:center;justify-content:space-between;padding:0 6px}
.nav a{color:#fff;font-size:12px;text-decoration:none;padding:7px 12px}
.nav a.current{background:#fff;color:var(--navy);font-weight:600}
.brand{position:absolute;top:150px;left:0;right:0;text-align:center}
.brand .mark{display:block;width:92px;height:92px;margin:0 auto 14px;border:3px solid #fff;background:var(--navy)}
.brand .name{font-family:var(--sans);font-weight:600;color:#fff;font-size:15px;letter-spacing:3px;text-transform:uppercase}
.hero h1{position:absolute;top:382px;left:0;right:0;text-align:center;font-family:var(--serif);font-weight:400;color:#fff;font-size:42px;letter-spacing:1px}
.hero .btn{position:absolute;top:470px;left:50%;transform:translateX(-50%)}
.values{position:absolute;top:588px;left:0;right:0;height:44px;background:rgba(13,31,58,.55);display:flex;justify-content:center;align-items:center;gap:0}
.values li{list-style:none;color:#fff;font-size:13px;letter-spacing:2px;padding:0 42px;border-right:1px solid rgba(255,255,255,.4)}
.values li:last-child{border:0}

/* practice */
.practice{height:940px;padding-top:38px}
.practice .lead{margin-top:26px}
.cards{position:absolute;top:308px;left:160px;width:880px;display:grid;grid-template-columns:repeat(3,280px);gap:60px 20px}
.card{position:relative;height:250px;border:1.5px solid var(--navy);border-radius:8px;padding:56px 34px 0}
.card .icon{position:absolute;top:-22px;left:24px;width:48px;height:48px;border-radius:50%;background:#fff;border:1.5px solid var(--navy);display:flex;align-items:center;justify-content:center}
.card h3{font-family:var(--sans);font-weight:600;font-size:15px;color:var(--ink);margin-bottom:8px}
.card p{font-size:12px;color:var(--muted);line-height:1.6}
.card .more{position:absolute;bottom:22px;left:0;right:0;text-align:center;color:var(--red);font-weight:700;font-size:11px;letter-spacing:1px}

/* testimonials */
.testimonials{height:590px}
.testimonials .bg{position:absolute;inset:0;background:linear-gradient(180deg,#d9dde3 0%,#eceef1 60%,#f4f5f7 100%)}
.testimonials .heading{position:relative;padding-top:100px}
.quotes{position:absolute;top:200px;left:160px;width:880px;display:grid;grid-template-columns:repeat(3,1fr);gap:28px}
.quote{background:#fff;height:290px;padding:90px 26px 0;box-shadow:0 4px 16px rgba(0,0,0,.08);position:relative}
.quote .avatar{position:absolute;top:22px;left:22px;width:60px;height:60px;border-radius:50%;background:linear-gradient(135deg,#b89b86,#6d5a4e)}
.quote h4{position:absolute;top:36px;left:96px;font-weight:600;font-size:15px;color:var(--ink)}
.quote p{font-size:12px;color:var(--muted)}
.quote.featured{background:var(--navy-dark)}
.quote.featured h4{color:#fff}
.quote.featured p{color:#c9d3e2}
.dots{position:absolute;top:540px;left:0;right:0;display:flex;justify-content:center;gap:10px}
.dots i{width:12px;height:12px;border-radius:50%;border:2px solid var(--navy)}
.dots i.on{background:var(--navy)}

/* about */
.about{height:670px;background:var(--navy-dark)}
.about .wedge{position:absolute;top:0;left:0;width:1200px;height:80px}
.about-text{position:absolute;top:110px;left:150px;width:500px;color:#d6deea;font-size:12.5px}
.about-text h2{font-family:var(--serif);font-weight:400;color:#fff;font-size:34px;margin-bottom:18px}
.about-text p{margin-bottom:16px}
.about-text .btn{margin-top:8px}
.attorney{position:absolute;top:70px;left:700px;width:320px;height:600px;background:linear-gradient(180deg,#3a5480 0%,#2a4f9a 55%,#1e3f85 100%);border-radius:160px 160px 0 0}

/* no charges */
.guarantee{height:230px;padding-top:40px}
.guarantee .heading{font-size:26px;margin-bottom:14px}

/* results */
.results{height:690px}
.results .bg{position:absolute;inset:0;background:linear-gradient(180deg,#eef0f3,#e3e6eb)}
.results .heading{position:relative;margin-top:90px;font-size:36px}
.results .lead{position:relative;margin-top:24px}
.stats{position:absolute;top:330px;left:170px;width:860px;display:grid;grid-template-columns:repeat(4,1fr)}
.stat{text-align:center;border-right:1px solid var(--line);padding:0 20px}
.stat:last-child{border:0}
.stat b{display:block;font-family:var(--serif);font-weight:400;font-size:34px;color:var(--navy);line-height:1.1}
.stat small{display:block;font-size:11px;color:var(--navy);margin-bottom:10px}
.stat span{display:block;font-size:11.5px;color:var(--muted);border-top:1px solid var(--line);padding-top:8px}
.results .btn{position:absolute;top:590px;left:50%;transform:translateX(-50%)}

/* contact */
.contact{height:640px;background:linear-gradient(90deg,#8a8d91 0%,#a9abae 40%,#7b7e82 100%)}
.statue{position:absolute;top:0;right:0;width:430px;height:640px;background:radial-gradient(ellipse at 50% 55%,#8a5a2e 0%,#5c3b20 45%,rgba(60,40,25,0) 75%)}
.form{position:absolute;top:30px;left:460px;width:290px;height:540px;background:rgba(255,255,255,.88);padding:26px 26px}
.form h2{font-family:var(--serif);font-weight:400;text-transform:uppercase;color:var(--navy);text-align:center;font-size:16px;line-height:1.45;margin-bottom:18px}
.field{height:32px;border:1px solid #c8cdd5;background:#fff;font-size:11px;color:#9aa1ab;padding:7px 10px;margin-bottom:12px}
.field.area{height:110px}
.form .btn{display:block;text-align:center;margin:4px 0 10px}
.form small{display:block;font-size:9.5px;color:var(--muted);text-align:center;line-height:1.5}

/* footer */
.site-footer{height:240px;background:var(--navy)}
.f-brand{position:absolute;top:24px;left:150px;text-align:center;width:140px}
.f-brand .mark{display:block;width:56px;height:56px;border:2px solid #fff;margin:0 auto 8px}
.f-brand .name{display:block;color:#fff;font-size:10px;letter-spacing:2px;font-weight:600;line-height:1.3}
.social{position:absolute;top:122px;left:150px;display:flex;gap:8px}
.social i{width:18px;height:18px;border-radius:50%;background:#fff}
.f-areas{position:absolute;top:150px;left:150px;width:320px;color:#cfd8e6;font-size:11px;line-height:1.55}
.f-title{font-family:var(--serif);color:#fff;font-size:13px;text-transform:uppercase;margin-bottom:4px}
.f-practice{position:absolute;top:26px;left:560px;width:500px;color:#cfd8e6;font-size:11px}
.f-practice .cols{display:grid;grid-template-columns:1fr 1fr;gap:0 40px;margin-top:6px}
.f-practice li{list-style:none;line-height:1.75}
.f-practice li.sub{padding-left:12px}
.f-practice li.sub::before{content:"– "}
.disclaimer{height:112px;background:var(--navy-deep);color:#8e9bb0;font-size:9.5px;padding:18px 150px}
.disclaimer h5{color:#fff;font-size:11px;letter-spacing:1px;margin-bottom:4px}
</style>
</head>
<body>

<header class="hero">
  <div class="hero-photo" role="img" aria-label="Photograph of the legal team standing in front of the firm's office"></div>
  <div class="hero-shade"></div>
  <div class="topbar">
    <div class="call">Call Us Now <b>(512) 555-0148</b></div>
    <div class="lang"><span>EN</span><span>ES</span></div>
  </div>
  <nav class="nav">
    <a class="current">Home</a><a>About Us</a><a>Practice Areas</a><a>Resources</a><a>Testimonials</a><a>Results</a><a>Media</a><a>Referring Attorneys</a><a>Giving Back</a><a>Contact Us</a>
  </nav>
  <div class="brand"><span class="mark"></span><span class="name">Velton Brisk Law, PLLC</span></div>
  <h1>AUSTIN ACCIDENT LAW FIRM</h1>
  <a class="btn">Request Free Consultation</a>
  <ul class="values"><li>INTEGRITY</li><li>COMPASSION</li><li>TRUST</li><li>ADVOCACY</li><li>RESULTS</li></ul>
</header>

<section class="practice">
  <h2 class="heading">Your Austin Personal Injury Lawyers</h2>
  <p class="lead">With over twenty years of combined experience in successfully handling hundreds of personal injury and accident cases, Austin Attorney Megan Velton Brisk and her staff are ready to protect you and your loved ones with the justice you deserve. Velton Brisk Law represents individuals, workers and families who suffer serious personal injury and wrongful death claims, including but not limited to:</p>
  <div class="cards">
    <article class="card"><span class="icon"><svg width="26" height="18" viewBox="0 0 26 18"><path d="M3 11l3-7h14l3 7v5H3z" fill="none" stroke="#1d3b66" stroke-width="1.6"/><circle cx="7.5" cy="15" r="2" fill="#1d3b66"/><circle cx="18.5" cy="15" r="2" fill="#1d3b66"/></svg></span><h3>Car Accidents</h3><p>Hurt in a crash on an Austin road? We gather the evidence and deal with insurers so you can focus on recovery.</p><span class="more">LEARN MORE</span></article>
    <article class="card"><span class="icon"><svg width="22" height="20" viewBox="0 0 22 20"><rect x="1" y="5" width="20" height="14" fill="none" stroke="#1d3b66" stroke-width="1.6"/><path d="M7 5V1h8v4" fill="none" stroke="#1d3b66" stroke-width="1.6"/></svg></span><h3>Workplace Accidents</h3><p>Injured on the job site or at work? We help you claim the full benefits and damages owed to you.</p><span class="more">LEARN MORE</span></article>
    <article class="card"><span class="icon"><svg width="20" height="20" viewBox="0 0 20 20"><path d="M2 6l8-4 8 4v9l-8 4-8-4z M2 6l8 4 8-4 M10 10v9" fill="none" stroke="#1d3b66" stroke-width="1.6"/></svg></span><h3>Product Liability</h3><p>When a defective product causes harm, the maker can be held responsible for your losses.</p><span class="more">LEARN MORE</span></article>
    <article class="card"><span class="icon"><svg width="28" height="18" viewBox="0 0 28 18"><path d="M1 3h16v11H1z M17 7h6l4 4v3H17z" fill="none" stroke="#1d3b66" stroke-width="1.6"/><circle cx="6" cy="15" r="2" fill="#1d3b66"/><circle cx="22" cy="15" r="2" fill="#1d3b66"/></svg></span><h3>Truck Accidents</h3><p>Collisions with 18-wheelers bring severe injuries. We take on trucking companies and their insurers.</p><span class="more">LEARN MORE</span></article>
    <article class="card"><span class="icon"><svg width="20" height="20" viewBox="0 0 20 20"><path d="M10 2v16 M4 8h12" fill="none" stroke="#1d3b66" stroke-width="1.8"/></svg></span><h3>Wrongful Death</h3><p>Losing a loved one is devastating. We pursue justice and compensation for grieving families.</p><span class="more">LEARN MORE</span></article>
    <article class="card"><span class="icon"><svg width="20" height="20" viewBox="0 0 20 20"><rect x="2" y="2" width="16" height="16" rx="3" fill="none" stroke="#1d3b66" stroke-width="1.6"/><path d="M10 6v8 M6 10h8" stroke="#1d3b66" stroke-width="1.8"/></svg></span><h3>Personal Injuries</h3><p>Slips, falls, dog bites and more. If someone else was careless, we help you recover.</p><span class="more">LEARN MORE</span></article>
  </div>
</section>

<section class="testimonials">
  <div class="bg" role="img" aria-label="Soft photograph of the firm's office interior"></div>
  <h2 class="heading">Client Testimonials</h2>
  <div class="quotes">
    <article class="quote featured"><span class="avatar" role="img" aria-label="Portrait of client Nora Ellison"></span><h4>Nora Ellison</h4><p>The team kept me informed every step of the way and treated my family with real care. I felt heard from our first call until my case settled. I could not ask for better.</p></article>
    <article class="quote"><span class="avatar" role="img" aria-label="Portrait of client Owen Hartley"></span><h4>Owen Hartley</h4><p>After my truck accident I did not know where to turn. They handled the insurers, answered every question and got a result far beyond what I expected.</p></article>
    <article class="quote"><span class="avatar" role="img" aria-label="Portrait of client Clara Dunmore"></span><h4>Clara Dunmore</h4><p>Honest, patient and tireless. Megan and her staff made a hard time easier, and I recommend them to anyone who needs a trusted advocate.</p></article>
  </div>
  <div class="dots"><i class="on"></i><i></i><i></i></div>
</section>

<section class="about">
  <svg class="wedge" viewBox="0 0 1200 80" preserveAspectRatio="none"><polygon points="0,0 1200,0 1200,10 0,70" fill="#f4f5f7"/></svg>
  <div class="about-text">
    <h2>ABOUT US</h2>
    <p>Led by the honest, tenacious, and compassionate Megan Velton Brisk, the Velton Brisk Law staff knows how to deliver positive results for clients. With a history of success, Velton Brisk Law, PLLC is ready to protect victims facing unexpected injury or death in Austin.</p>
    <p>As the victim of a serious injury herself, Megan Velton Brisk understands how a single moment can change everything. When a tragedy occurs, families can be affected by physical and emotional pain, as well as financial stress.</p>
    <p>You do not have to face the challenges of a life-changing injury or an unjust death by yourself. Let the Austin injury lawyer from Velton Brisk Law, PLLC be your fighting chance. Despite the difficulties that lie ahead of you, Velton Brisk Law is committed to providing you with the compassion and justice you deserve.</p>
    <a class="btn">Learn More</a>
  </div>
  <div class="attorney" role="img" aria-label="Photograph of attorney Megan Velton Brisk in a blue blazer"></div>
</section>

<section class="guarantee">
  <h2 class="heading">There Are No Charges Unless Your Case Is Won</h2>
  <p class="lead">We understand the financial burden you may be suffering during this difficult time. That's why we do not charge unless we win your case. Velton Brisk Law goes to great lengths to help you secure the compensation you deserve.</p>
</section>

<section class="results">
  <div class="bg" role="img" aria-label="Faint photograph of a courtroom in light grey tones"></div>
  <h2 class="heading">Recent Case Results</h2>
  <p class="lead">It's the simple things that make the difference. At Velton Brisk Law, you are more than a client. You are a priority. Our staff will do everything possible so that you and your loved ones are well cared for. Our staff handles all the unpleasant tasks involved in being involved in a serious Austin accident. You and your case are important at Velton Brisk Law, PLLC.</p>
  <div class="stats">
    <div class="stat"><b>2.2</b><small>Million</small><span>Workplace Injury Settlement</span></div>
    <div class="stat"><b>4.1</b><small>Million</small><span>Wrongful Death Settlement</span></div>
    <div class="stat"><b>2</b><small>Million</small><span>Truck Accident Settlement</span></div>
    <div class="stat"><b>1.5</b><small>Million</small><span>Product Liability Settlement</span></div>
  </div>
  <a class="btn">View Case Studies</a>
</section>

<section class="contact">
  <div class="statue" role="img" aria-label="Photograph of a bronze statue of Lady Justice holding scales"></div>
  <form class="form">
    <h2>Contact Us Today<br>For A Free Case Review</h2>
    <div class="field">First Name</div>
    <div class="field">Last Name</div>
    <div class="field">Phone Number</div>
    <div class="field">Email Address</div>
    <div class="field area">Tell us your story</div>
    <a class="btn">Send</a>
    <small>Your details stay private and are used only to review your case. Our Privacy Policy and Terms of Use apply.</small>
  </form>
</section>

<footer class="site-footer">
  <div class="f-brand"><span class="mark"></span><span class="name">VELTON BRISK LAW, PLLC</span></div>
  <div class="social"><i></i><i></i><i></i><i></i><i></i><i></i></div>
  <div class="f-areas">
    <div class="f-title">Areas We Serve</div>
    Bastrop · Bee Cave · Buda · Cedar Park · Kyle · Lake Travis · Lakeway · Leander · Manchaca · Manor · Pflugerville · Rollingwood · Round Rock · San Marcos · Westlake
  </div>
  <div class="f-practice">
    <div class="f-title">Areas of Practice</div>
    <div class="cols">
      <ul><li>Auto Accidents</li><li class="sub">Commercial Vehicle Accidents</li><li class="sub">Distracted Driver Accidents</li><li class="sub">Drunk Driving</li><li class="sub">Pedestrian Accidents</li><li>Child Abuse</li><li>Personal Injury Attorney in Austin</li><li class="sub">Brain Injuries</li><li class="sub">Dog Bites</li></ul>
      <ul><li>Product Liability</li><li>Sexual Assault</li><li>Workplace Injury</li><li class="sub">Construction Accidents</li><li class="sub">Slip and Fall</li><li>Wrongful Death</li><li>Car Accident FAQs</li></ul>
    </div>
  </div>
</footer>

<div class="disclaimer">
  <h5>DISCLAIMER</h5>
  <p>The information on this website is for general information purposes only. Nothing on this site should be taken as legal advice for any individual case or situation. This information is not intended to create, and receipt or viewing does not constitute, an attorney-client relationship. Past results do not guarantee future outcomes.</p>
  <p>© Velton Brisk Law, PLLC. All rights reserved.</p>
</div>

</body>
</html>
```